Executive Summary

Create a one page executive summary of a venture fund - with the information here:
https://files.brindlecove.net/d/7qTm3VxR9pLw2KcYhN8sD4fBzJ6gA1eUoXiM5tQrWnE/view?share=open

```html
<!DOCTYPE html>
<html lang="en">
<head>
<meta charset="utf-8">
<title>Executive Summary – Northpine Capital</title>
<link rel="stylesheet" href="https://fonts.googleapis.com/css2?family=Gelasio:wght@400;500&family=Mulish:wght@400;600;700;800&display=swap">
<style>
  :root {
    --maroon: #7f1427;
    --tan: #a99b8c;
    --ink: #3a3a3a;
    --paper: #ffffff;
    --footer: #f3f2f0;
    --rule: #dddddd;
  }
  * { box-sizing: border-box; margin: 0; padding: 0; }
  html, body { width: 950px; height: 1200px; overflow: hidden; background: var(--paper); }
  body { font-family: "Mulish", sans-serif; color: var(--ink); }
  .page { position: relative; width: 950px; height: 1200px; background: var(--paper); overflow: hidden; }

  .header-swoosh { position: absolute; top: 0; left: 0; width: 950px; height: 320px; }
  .doc-title {
    position: absolute; right: 16px; top: 17px; text-align: right;
    color: #fff; font-weight: 800; font-size: 37px; line-height: 48px;
  }

  .portrait {
    position: absolute; left: 41px; top: 121px; width: 164px; height: 164px;
    border-radius: 50%; border: 1px solid #555;
    background: radial-gradient(circle at 50% 45%, #d9b49e 0%, #8a6a5a 45%, #1d1a1a 80%);
  }
  .profile { position: absolute; left: 245px; top: 119px; width: 400px; }
  .profile-name { font-family: "Gelasio", serif; color: var(--maroon); font-size: 24px; line-height: 30px; font-weight: 400; }
  .profile-role { font-family: "Gelasio", serif; color: var(--maroon); font-size: 17px; line-height: 24px; margin-top: 1px; }
  .profile-bio { font-size: 16px; line-height: 27px; margin-top: 7px; width: 395px; }

  .body-text { position: absolute; left: 33px; width: 895px; font-size: 16px; line-height: 27px; }
  .lorem { width: 830px; }
  .intro { top: 305px; }
  .closing { top: 950px; }

  .section-title { position: absolute; left: 33px; font-family: "Gelasio", serif; color: var(--maroon); font-size: 25px; line-height: 32px; font-weight: 400; }
  .portfolio-title { top: 420px; }
  .sub-title { position: absolute; left: 33px; font-family: "Gelasio", serif; color: var(--maroon); font-size: 18px; line-height: 24px; font-weight: 400; }
  .startup-title { top: 468px; }
  .fund-title { top: 732px; }

  .startup-desc { top: 497px; }
  .testimonial { top: 641px; }

  .fund-list { position: absolute; left: 33px; top: 757px; list-style: none; font-size: 16px; line-height: 27.3px; }
  .fund-list li { position: relative; padding-left: 19px; }
  .fund-list li::before {
    content: ""; position: absolute; left: 0; top: 11px;
    border-left: 4px solid var(--maroon); border-top: 3px solid transparent; border-bottom: 3px solid transparent;
  }

  .contact-band { position: absolute; left: 0; top: 1067px; width: 950px; height: 133px; background: var(--footer); }
  .join-title { position: absolute; left: 28px; top: 15px; font-family: "Gelasio", serif; color: var(--maroon); font-size: 24px; line-height: 30px; font-weight: 400; }
  .join-rule { position: absolute; left: 30px; top: 52px; width: 515px; height: 1px; background: var(--rule); }
  .inquiry { position: absolute; left: 28px; top: 64px; font-size: 15px; line-height: 24px; }
  .inquiry strong { font-weight: 700; font-size: 13.5px; }
  .phone { position: absolute; left: 389px; top: 76px; display: flex; align-items: center; gap: 8px; font-size: 17.5px; font-weight: 700; letter-spacing: 0.3px; }
  .contact-icon { position: absolute; left: 832px; top: 6px; width: 90px; height: 122px; }
</style>
</head>
<body>
<main class="page">
  <svg class="header-swoosh" viewBox="0 0 950 320" aria-hidden="true">
    <path d="M0 0 C520 20 880 110 950 318 L950 255 C860 110 560 25 0 0 Z" fill="var(--tan)"/>
    <path d="M0 0 C560 22 870 105 950 250" fill="none" stroke="#fff" stroke-width="3"/>
    <path d="M0 0 L950 0 L950 246 C860 100 560 20 0 0 Z" fill="var(--maroon)"/>
  </svg>
  <h1 class="doc-title">Executive<br>Summary</h1>

  <div class="portrait" role="img" aria-label="Portrait photo of Mira Lensky"></div>
  <section class="profile">
    <h2 class="profile-name">Mira Lensky</h2>
    <p class="profile-role">CFA, Vice President (California)</p>
    <p class="profile-bio">Veteran investor in energy transition. 10+ years of experience in capital markets, energy, sustainability and innovations. M.S. from Halbrook University</p>
  </section>

  <p class="body-text lorem intro">Lorem ipsum dolor sit amet, consectetuer adipiscing elit, sed diam nonummy lorem nibh euismod tincidunt ut laoreet dolore magna aliquam erat volutpat. Ut wisi enim ad minim veniam, quis nostrud exerci tation ummy ullamcorper suscipit lobortis nisl ut aliquip ex ea commodo consequat.</p>

  <h2 class="section-title portfolio-title">Example Portfolio Startups</h2>
  <h3 class="sub-title startup-title">Solvantra: Modular Green Methanol Production</h3>
  <div class="body-text startup-desc">
    <p>The Corwell Spin out company has developed a proprietary process to synthesize commodity chemicals, starting with green methanol and ammonia, at cost-parity using used diesel engines.</p>
    <p>By converting these engines to consume inputs such as methane, biogas, and carbon dioxide, the company has created a low-carbon process to produce these chemicals by displacing the need for flaring or release of methane, plugging into waste streams offsite.</p>
  </div>
  <p class="body-text testimonial">It has been a pleasure working with Northpine Capital and having them on our cap table. Their team is well connected, always available and eager to help.</p>

  <h3 class="sub-title fund-title">Fund I Investments So Far (Continue )to Invest</h3>
  <ul class="fund-list">
    <li>Lumarex, former Brightfilm Labs (Seed, raising Series A)</li>
    <li>Solvantra (Seed, raising Series A)</li>
    <li>Carbonwell (Series A, will raise Series B)</li>
    <li>Feralyn (Seed)</li>
    <li>Verdane Fuels (Pre-seed)</li>
    <li>ChargeLoop (Seed)</li>
  </ul>

  <p class="body-text lorem closing">Lorem ipsum dolor sit amet, consectetuer adipiscing elit, sed diam nonummy lorem nibh euismod tincidunt ut laoreet dolore magna aliquam erat volutpat. Ut wisi enim ad minim veniam, quis nostrud exerci tation ummy ullamcorper suscipit lobortis nisl ut aliquip ex ea commodo consequat.</p>

  <footer class="contact-band">
    <h2 class="join-title">Join Us</h2>
    <div class="join-rule"></div>
    <p class="inquiry">For Any Inquiries, Please Contact:<br><strong>Tessa Varn, Managing Partner</strong></p>
    <p class="phone">
      <svg width="22" height="22" viewBox="0 0 24 24" aria-hidden="true" fill="none" stroke="#444" stroke-width="1.4" stroke-linejoin="round">
        <path d="M5 3 L8.5 3 L10 7.5 L8 9 C9 11.5 12.5 15 15 16 L16.5 14 L21 15.5 L21 19 C21 20 20 21 19 21 C10.5 20.5 3.5 13.5 3 5 C3 4 4 3 5 3 Z"/>
        <path d="M14 3.5 A7 7 0 0 1 20.5 10"/>
        <path d="M13.5 6.5 A4 4 0 0 1 17.5 10.5"/>
      </svg>
      555.010.4821
    </p>
    <svg class="contact-icon" viewBox="0 0 90 122" aria-hidden="true" fill="none" stroke="var(--maroon)" stroke-width="3" stroke-linejoin="round" stroke-linecap="round">
      <path d="M12 2 L82 2 L82 14 L12 14 C6 14 6 24 12 24 L82 24"/>
      <path d="M6 14 L6 114 C6 118 8 120 12 120 L82 120 L82 14"/>
      <line x1="12" y1="8" x2="82" y2="8"/>
      <circle cx="48" cy="62" r="20"/>
      <circle cx="48" cy="56" r="7"/>
      <path d="M35 76 C38 68 58 68 61 76"/>
      <line x1="36" y1="92" x2="60" y2="92"/>
      <line x1="40" y1="100" x2="56" y2="100"/>
    </svg>
  </footer>
</main>
</body>
</html>
```